corvapinecare needs a 4.6 handout

i need a styalized 4x6 postcard sized handout to leave on cars at shopping plazas and apartment buildings. WE are a medical marijuana referal clinic in brockton MA and we write perscriptions for qualifying patients, i have attached a pdf file of the content i need included in the hand out but please do not limit yourself if you feel like you could word it better. it is important to have our contact info front and center
Target Market(s)
potential medical marijuana patients
Industry/Entity Type
Apartment
Requirements
Must have
- the content listed inside the PDF file i attached
Nice to have
- must have everything in the PDF file. should be colorful and eye catching while still looking professional
Should not have
- pictures of cannabis buds or flowering plants.

```html
<!DOCTYPE html>
<html lang="en">
<head>
<meta charset="utf-8">
<title>CorvaPine Care – Medical Marijuana Evaluations Handout</title>
<link rel="stylesheet" href="https://fonts.googleapis.com/css2?family=Bebas+Neue&family=Tinos:wght@700&display=swap">
<style>
  :root {
    --page-bg: #e9e6e1;
    --leaf-dark: #0f2410;
    --leaf-mid: #2f5a22;
    --leaf-light: #4f8a33;
    --sky-blue: #62cff4;
    --pale-blue: #a9d4f5;
    --white: #ffffff;
    --band: #0b150c;
  }
  * { box-sizing: border-box; margin: 0; padding: 0; }
  html, body {
    width: 1200px; height: 1000px; overflow: hidden;
    background: var(--page-bg);
  }
  .postcard {
    position: absolute; left: 70px; top: 140px;
    width: 1060px; height: 720px;
    overflow: hidden;
    box-shadow: 0 6px 18px rgba(0,0,0,.35);
  }
  .foliage-backdrop {
    position: absolute; inset: 0 0 88px 0;
    background:
      radial-gradient(ellipse at 20% 70%, var(--leaf-light) 0%, transparent 45%),
      radial-gradient(ellipse at 85% 75%, var(--leaf-light) 0%, transparent 40%),
      radial-gradient(ellipse at 55% 20%, var(--leaf-mid) 0%, transparent 55%),
      linear-gradient(180deg, var(--leaf-dark) 0%, var(--leaf-mid) 60%, #3d6e2a 100%);
  }
  .headline-frame {
    position: absolute; left: 105px; top: 78px;
    width: 852px; height: 157px;
    border: 2px solid var(--sky-blue);
    outline: 1px solid rgba(98,207,244,.6); outline-offset: -7px;
    background: rgba(0,0,0,.28);
    display: flex; flex-direction: column; justify-content: center; align-items: center;
  }
  .headline {
    font-family: "Bebas Neue", sans-serif;
    color: var(--sky-blue);
    font-size: 62px; line-height: 1.0; letter-spacing: .5px;
    text-align: center;
    text-shadow: 2px 2px 3px rgba(0,0,0,.7);
  }
  .hours {
    position: absolute; left: 95px; top: 310px; width: 280px;
    text-align: center;
    font-family: "Tinos", serif; font-weight: 700;
    color: var(--white); font-size: 26px; line-height: 37.5px;
    text-shadow: 2px 2px 3px rgba(0,0,0,.8);
  }
  .hours-title { color: var(--pale-blue); font-size: 30px; }
  .brand-seal {
    position: absolute; left: 412px; top: 296px;
    width: 236px; height: 236px; border-radius: 50%;
    background: rgba(255,255,255,.92);
    display: flex; align-items: center; justify-content: center;
  }
  .brand-name {
    font-family: "Tinos", serif; font-weight: 700;
    font-size: 38px; color: #2a5f8f;
  }
  .qualify-note {
    position: absolute; left: 650px; top: 310px; width: 350px;
    text-align: center;
    font-family: "Tinos", serif; font-weight: 700;
    color: var(--white); font-size: 23px; line-height: 30px;
    text-shadow: 2px 2px 3px rgba(0,0,0,.8);
  }
  .qualify-note .count { color: var(--pale-blue); font-size: 31px; }
  .contact-band {
    position: absolute; left: 0; bottom: 0;
    width: 100%; height: 88px;
    background: var(--band);
    border-top: 2px solid var(--sky-blue);
    display: flex; align-items: center; justify-content: center;
    font-family: "Bebas Neue", sans-serif;
    color: var(--pale-blue); font-size: 42px; letter-spacing: .5px;
  }
  .contact-band .divider { margin: 0 16px; }
</style>
</head>
<body>
  <main class="postcard">
    <div class="foliage-backdrop" role="img" aria-label="Dense green cannabis leaf foliage filling the card background"></div>

    <div class="headline-frame">
      <h1 class="headline">Do you need a medical marijuana card?<br>We do medical marijuana evaluations!</h1>
    </div>

    <section class="hours">
      <p class="hours-title">HOURS:</p>
      <p>TUESDAY: 9 - 5</p>
      <p>WEDNESDAY: 9 - 5</p>
      <p>THURSDAY: 9 - 6</p>
      <p>FRIDAY: 9 - 7</p>
      <p>SATURDAY: 9 - 3</p>
    </section>

    <div class="brand-seal">
      <span class="brand-name">CorvaPine</span>
    </div>

    <p class="qualify-note">
      There are over <span class="count">200</span><br>
      qualifying conditions<br>
      in the state of<br>
      Massachusetts,<br>
      call today to see if<br>
      you qualify and book an<br>
      appointment!
    </p>

    <footer class="contact-band">
      <span>WWW.CORVAPINECARE.NET</span><span class="divider">|</span><span>774-555-0148</span>
    </footer>
  </main>
</body>
</html>
```